Business Card Design Project Lend Aid

Simple and clean business card,

Logo and fond added in attachment

Data need to be changable:
Ria Vondeck
Customer Service Specialist

Lend Aid - ria.vondeck@lendaid.be - Mob: +32491532876 - www.lendaid.be

Target Market(s)

Small businesses

Industry/Entity Type

Business

Requirements
Nice to have
• QR-code

```html
<!DOCTYPE html>
<html lang="en">
<head>
<meta charset="utf-8">
<title>Lend Aid – Business Card</title>
<link rel="stylesheet" href="https://fonts.googleapis.com/css2?family=Cinzel:wght@600;700&family=Arimo:wght@700&display=swap">
<style>
  :root {
    --card-bg: #e0f4f4;
    --brand-green: #88ff0a;
    --brand-cyan: #4fc8f4;
    --text-cyan: #8eecf6;
    --rule-cyan: #a4e6ee;
    --url-ink: #111111;
  }
  html, body {
    margin: 0;
    padding: 0;
    overflow: hidden;
    background: var(--card-bg);
  }
  .card {
    position: relative;
    width: 1200px;
    height: 686px;
    background: var(--card-bg);
    overflow: hidden;
    font-family: "Cinzel", serif;
  }
  .brand {
    position: absolute;
    left: 72px;
    top: 236px;
    display: flex;
    align-items: center;
    gap: 30px;
  }
  .brand-square {
    width: 150px;
    height: 150px;
    border-radius: 0;
    background: var(--brand-cyan);
  }
  .brand-name {
    font-family: "Cinzel", serif;
    font-weight: 700;
    font-size: 66px;
    line-height: 1;
    color: var(--brand-green);
    letter-spacing: 1px;
    white-space: nowrap;
  }
  .divider {
    position: absolute;
    left: 725px;
    top: 134px;
    width: 2px;
    height: 392px;
    background: var(--rule-cyan);
  }
  .contact {
    position: absolute;
    left: 766px;
    top: 222px;
    width: 370px;
    color: var(--text-cyan);
    font-weight: 700;
  }
  .contact-name {
    margin: 0;
    text-align: right;
    font-size: 46px;
    line-height: 1;
    letter-spacing: 1px;
    white-space: nowrap;
  }
  .contact-role {
    margin: 24px 0 0;
    font-size: 25px;
    line-height: 1;
    font-weight: 600;
    white-space: nowrap;
  }
  .contact-email,
  .contact-phone {
    margin: 0;
    font-size: 22px;
    line-height: 1;
    letter-spacing: 1px;
    white-space: nowrap;
    text-transform: uppercase;
  }
  .contact-email { margin-top: 26px; }
  .contact-phone { margin-top: 44px; }
  .footer-band {
    position: absolute;
    left: 0;
    bottom: 0;
    width: 1200px;
    height: 96px;
    background: var(--brand-green);
  }
  .footer-url {
    position: absolute;
    left: 0;
    top: 10px;
    width: 1194px;
    text-align: center;
    font-family: "Arimo", sans-serif;
    font-weight: 700;
    font-size: 22px;
    color: var(--url-ink);
    letter-spacing: 0.5px;
  }
</style>
</head>
<body>
  <main class="card">
    <div class="brand">
      <div class="brand-square"></div>
      <div class="brand-name">Lend Aid</div>
    </div>

    <div class="divider"></div>

    <section class="contact">
      <h1 class="contact-name">Ria Vondeck</h1>
      <p class="contact-role">Customer Service Specialist</p>
      <p class="contact-email">ria.vondeck@lendaid.be</p>
      <p class="contact-phone">Mob: +32491532876</p>
    </section>

    <footer class="footer-band">
      <div class="footer-url">WWW.LENDAID.BE</div>
    </footer>
  </main>
</body>
</html>
```